Fresh Start Body Quest 2017 Poster

We are having a Fresh Start, Body Quest for 2017 at our fitness studio. We need a poster design using the template attached as a reference (Only reference). I have also included our Drovelux logo to put on the poster. Please DO NOT use the graphics in the flyer as we are expecting something much much better :-)
MUST HAVES:
- Size needed 11x17 with bleeding for printing
- .PSD File Format WITH LAYERS (CS3 Compatible)*** A MUST
- Use Drovelux Bootcamps Logo
- Use Information in the attached word doc

```html
<!DOCTYPE html>
<html lang="en">
<head>
<meta charset="utf-8">
<title>Fresh Start, Body Quest 2017 Poster</title>
<link href="https://fonts.googleapis.com/css2?family=Oswald:wght@500;700&family=Roboto+Condensed:wght@700&family=Titillium+Web:wght@600&family=Open+Sans:wght@400;700&display=swap" rel="stylesheet">
<style>
  :root {
    --charcoal: #1c1c1c;
    --charcoal-light: #333333;
    --photo-dark: #2a2a2a;
    --photo-light: #8a8a8a;
    --blue: #3b86c9;
    --blue-dark: #2f6fab;
    --orange: #f39422;
    --white: #ffffff;
    --ink: #1b2430;
    --rule: #6f6f6f;
  }
  * { box-sizing: border-box; margin: 0; padding: 0; }
  html, body { width: 776px; height: 1200px; overflow: hidden; background: var(--charcoal); }
  .poster {
    position: relative;
    width: 776px;
    height: 1200px;
    overflow: hidden;
    background: radial-gradient(ellipse at 50% 45%, var(--charcoal-light) 0%, var(--charcoal) 70%);
    font-family: "Titillium Web", sans-serif;
    color: var(--white);
  }
  .hero-photo {
    position: absolute;
    left: 0; top: 0;
    width: 776px; height: 228px;
    background: linear-gradient(180deg, var(--photo-light) 0%, var(--photo-dark) 100%);
  }
  .hero-rule {
    position: absolute;
    left: 0; top: 226px;
    width: 776px; height: 2px;
    background: var(--blue);
  }
  .prize-badge {
    position: absolute;
    left: 584px; top: 94px;
    width: 176px; height: 118px;
  }
  .prize-badge svg { position: absolute; inset: 0; }
  .prize-text {
    position: relative;
    text-align: center;
    color: var(--ink);
    font-family: "Roboto Condensed", sans-serif;
    font-weight: 700;
    padding-top: 10px;
    line-height: 1;
  }
  .prize-amount { font-size: 50px; display: block; }
  .prize-label { font-size: 21px; display: block; line-height: 1.05; }
  .headline {
    position: absolute;
    left: 0; top: 188px;
    width: 776px;
    text-align: center;
    font-family: "Oswald", sans-serif;
    font-weight: 700;
    text-transform: uppercase;
    line-height: 0.98;
    text-shadow: 0 4px 8px rgba(0,0,0,0.6);
  }
  .headline-main { color: var(--white); font-size: 92px; display: block; }
  .headline-accent { color: var(--orange); font-size: 104px; display: block; margin-top: 22px; }
  .tagline {
    position: absolute;
    left: 0; top: 578px;
    width: 776px;
    text-align: center;
    font-family: "Roboto Condensed", sans-serif;
    font-weight: 700;
    font-size: 30px;
    line-height: 1.4;
  }
  .details {
    position: absolute;
    left: 136px; top: 682px;
    width: 504px; height: 254px;
    border-top: 1px solid var(--rule);
    border-bottom: 1px solid var(--rule);
    border-left: 1px solid #444;
  }
  .details::after {
    content: "";
    position: absolute;
    right: -2px; top: 10px;
    width: 1px; height: 236px;
    background: var(--blue);
  }
  .schedule {
    margin: 24px 0 0 22px;
    display: grid;
    grid-template-columns: 180px auto;
    font-size: 19px;
    line-height: 1.3;
  }
  .schedule dt { color: var(--orange); }
  .schedule dd { color: var(--white); }
  .details-divider {
    margin: 20px 0 0 14px;
    width: 486px; height: 1px;
    background: var(--blue);
  }
  .offer {
    display: flex;
    align-items: center;
    margin: 20px 0 0 22px;
  }
  .offer-text { color: var(--orange); font-size: 19px; line-height: 1.3; width: 290px; }
  .offer-price {
    font-family: "Open Sans", sans-serif;
    font-weight: 700;
    font-size: 58px;
    color: var(--white);
    margin-left: 14px;
  }
  .brand-name {
    position: absolute;
    left: 0; top: 990px;
    width: 776px;
    text-align: center;
    font-family: "Oswald", sans-serif;
    font-weight: 700;
    font-size: 48px;
    color: var(--white);
    text-transform: uppercase;
  }
  .footer-band {
    position: absolute;
    left: 0; top: 1100px;
    width: 776px; height: 100px;
  }
  .footer-band svg { position: absolute; inset: 0; }
  .footer-text {
    position: absolute;
    left: 0; top: 56px;
    width: 776px;
    text-align: center;
    font-family: "Open Sans", sans-serif;
    font-size: 20px;
    color: var(--ink);
    letter-spacing: 0.5px;
  }
  .footer-text strong { font-size: 25px; font-weight: 700; }
</style>
</head>
<body>
<main class="poster">
  <div class="hero-photo" role="img" aria-label="Black and white photo of people training in a gym with a tractor tire and floor exercises"></div>
  <div class="hero-rule"></div>

  <div class="prize-badge">
    <svg width="176" height="118" viewBox="0 0 176 118" aria-hidden="true">
      <path d="M8 6 L170 0 L166 40 L176 60 L168 112 L14 118 L0 84 L10 60 Z" fill="var(--blue)"/>
    </svg>
    <div class="prize-text">
      <span class="prize-amount">$500</span>
      <span class="prize-label">Cash Prize<br>for Winner!</span>
    </div>
  </div>

  <h1 class="headline">
    <span class="headline-main">Fresh Start,</span>
    <span class="headline-accent">Body Quest</span>
  </h1>

  <p class="tagline">In just 6 weeks, transform your body and<br>get in the best shape of your life!</p>

  <section class="details">
    <dl class="schedule">
      <dt>Kick Off Meeting:</dt><dd>Thursday, Jan 12th at 7:30pm</dd>
      <dt>Start Date:</dt><dd>Tuesday, January 17th</dd>
      <dt>End Date:</dt><dd>Saturday, February 25th</dd>
      <dt>Finale Party:</dt><dd>March 2nd</dd>
    </dl>
    <div class="details-divider"></div>
    <div class="offer">
      <p class="offer-text">6 Weeks of Training, Nutrition,<br>and Coaching Starting at just</p>
      <p class="offer-price">$99!</p>
    </div>
  </section>

  <p class="brand-name">Drovelux Bootcamps</p>

  <footer class="footer-band">
    <svg width="776" height="100" viewBox="0 0 776 100" aria-hidden="true">
      <path d="M0 18 L60 12 L120 20 L190 8 L260 16 L340 6 L420 18 L500 10 L580 20 L660 8 L730 16 L776 10 L776 100 L0 100 Z" fill="var(--blue)"/>
    </svg>
    <p class="footer-text">VISIT <strong>www.droveluxbootcamps.com</strong> FOR MORE INFO</p>
  </footer>
</main>
</body>
</html>
```